Qivera Health & Wellness Business Card Design

We would like to create business cards matching with our new logo design. The card should be professional looking but still have a playful side and something that would be eye catching. We are planing to open a luxury medical spa and looking to create a design based on this new logo. We are looking for a design that shows off luxury but not be gold in color. Also, while we are a more female oriented medical center we do have men that come in for our services and it should be be too feminine.

Target Market(s)

Health & Wellness. Medical patients. Luxury spa

Industry/Entity Type

Health And Wellness

Contact Information for Business Card

It should have the logo design in the front of card and back of card should have our contact information. Our current colors are peach/ coral, teal, and gray. We are looking for a modern looking design.

Font styles to use
Script

Colors
32a6d6
e667a6
86cfc6
fece3e

Requirements
Must have
• It should have our logo design. We would prefer to have a more modern look to the card.
Nice to have
• Eye-Catching Design on the personable side but still classy.
Should not have
• At this point we are looking for the best design. It should not have color purple.

```html
<!DOCTYPE html>
<html lang="en">
<head>
<meta charset="utf-8">
<title>Qivera Health &amp; Wellness – Business Card</title>
<link href="https://fonts.googleapis.com/css2?family=Roboto:wght@400;500&display=swap" rel="stylesheet">
<style>
  :root {
    --page: #b9b9b9;
    --card-dark: #2b2b2b;
    --card-light: #ffffff;
    --ink: #1f1f1f;
    --accent: #2fa3d6;
    --stripe: #1a1a1a;
    --on-dark: #ffffff;
  }
  * { margin: 0; padding: 0; box-sizing: border-box; }
  html, body {
    width: 1200px; height: 930px; overflow: hidden;
    background: var(--page);
    font-family: "Roboto", Arial, sans-serif;
  }
  .stage {
    width: 1200px; height: 930px;
    display: flex; flex-direction: column;
    align-items: center; justify-content: center; gap: 60px;
  }
  .card {
    position: relative;
    width: 600px; height: 343px;
    border-radius: 22px;
    overflow: hidden;
  }
  .card--back {
    background: var(--card-dark);
    display: flex; align-items: center; justify-content: center;
  }
  .brand-name {
    font-weight: 400;
    letter-spacing: 0.5px;
  }
  .card--back .brand-name { color: var(--on-dark); font-size: 30px; }
  .card--front { background: var(--card-light); color: var(--ink); }
  .card--front .brand-name {
    position: absolute; top: 52px; right: 44px;
    font-size: 20px; color: var(--ink);
  }
  .divider {
    position: absolute; top: 112px; left: 110px; right: 36px;
    height: 1px; background: var(--accent);
  }
  .person { position: absolute; left: 40px; top: 176px; }
  .person__name {
    font-size: 20px; font-weight: 500; color: var(--accent);
    text-transform: uppercase; letter-spacing: 0.3px;
  }
  .person__role { font-size: 15px; margin-top: 3px; }
  .person__rule { width: 236px; height: 1px; background: var(--accent); margin-top: 12px; }
  .contact { list-style: none; margin-top: 12px; }
  .contact li {
    display: flex; align-items: center; gap: 10px;
    font-size: 16px; line-height: 22px; letter-spacing: 0.3px;
  }
  .contact svg { width: 11px; height: 11px; fill: var(--accent); flex: none; }
  .address {
    position: absolute; right: 40px; top: 146px;
    text-align: right; font-size: 15px; line-height: 21px; letter-spacing: 0.3px;
  }
  .band { position: absolute; left: 0; bottom: 0; width: 600px; height: 343px; pointer-events: none; }
</style>
</head>
<body>
<main class="stage">
  <section class="card card--back" aria-label="Card back">
    <span class="brand-name">Qivera Health &amp; Wellness</span>
  </section>

  <section class="card card--front" aria-label="Card front">
    <span class="brand-name">Qivera Health &amp; Wellness</span>
    <div class="divider"></div>

    <div class="address">218b Marlow Street,<br>Ashford, NZ, 7042</div>

    <div class="person">
      <p class="person__name">Daniel Harlow</p>
      <p class="person__role">Director</p>
      <div class="person__rule"></div>
      <ul class="contact">
        <li><svg viewBox="0 0 12 12"><path d="M3 1l2 2.5-1 1.2c.7 1.4 1.8 2.5 3.2 3.2l1.2-1L11 9l-1 2C5 11 1 7 1 2z"/></svg>(555) 014-2290</li>
        <li><svg viewBox="0 0 12 12"><path d="M1 3h10v6H1zM2 4v.3L6 7l4-2.7V4z" fill-rule="evenodd"/></svg>info@qivera.com</li>
        <li><svg viewBox="0 0 12 12"><path d="M6 1a5 5 0 100 10A5 5 0 006 1zm0 1.2c.6.7 1 1.8 1.1 3.2H4.9C5 4 5.4 2.9 6 2.2zM2.3 6.6h1.5c.1 1.1.4 2 .8 2.7A3.8 3.8 0 012.3 6.6zm0-1.2a3.8 3.8 0 012.3-2.7c-.4.7-.7 1.6-.8 2.7zm3.7 4.4c-.6-.7-1-1.8-1.1-3.2h2.2C7 8 6.6 9.1 6 9.8zm1.4-.5c.4-.7.7-1.6.8-2.7h1.5a3.8 3.8 0 01-2.3 2.7zm.8-3.9c-.1-1.1-.4-2-.8-2.7a3.8 3.8 0 012.3 2.7z"/></svg>www.qivera.com</li>
      </ul>
    </div>

    <svg class="band" viewBox="0 0 600 343" aria-hidden="true">
      <path d="M0 333 L410 333 Q425 333 440 318 L460 300 Q475 287 500 287 L600 287 L600 343 L0 343 Z" fill="var(--accent)"/>
      <path d="M0 325 L405 325 Q418 325 430 313 L440 304 L442 306 L432 316 Q420 328 405 328 L0 328 Z" fill="var(--stripe)"/>
    </svg>
  </section>
</main>
</body>
</html>
```